Premium Fitness Meal Plan Design for VoltaKor (Brand Like PlumQuarry!)

VoltaKor 6 Week Autumn Forge Meal Plan Design (Branded Handout)

πŸ“„ Overview:
We are looking for a professionally designed, branded meal plan handout for our fitness facility, VoltaKor. This meal plan will be used during our upcoming 6 Week Autumn Forge Quest, where members aim to lose body fat, build lean muscle, and improve their energy through nutrition and strength training.

The design should be highly polished, visually engaging, and reflect our brand quality β€” something on par with what you would see from larger national gym chains (e.g., Plum Quarry, K62, Delmar’s Drillyard). This is not just a text document β€” we want it to feel premium, motivating, and easy to follow, ideally something members are excited to reference and share.

🧾 Format & Layout:
Size: Standard 8.5x11 inch format (single or double-sided)

Final Output: Print-ready PDF + editable source files

Orientation: Portrait

Can be designed as either:

One visually organized front-and-back sheet

Or two clean, digestible pages presented as a mini-handout

🎨 Design Style:
Clean, energetic, and transformation-focused

Use brand colors and fonts that feel bold, fresh, and motivating

Include icons, dividers, or visual cues to separate sections (not just blocks of text)

Sections should feel approachable and empowering, not clinical or restrictive

Include room for the VoltaKor logo (provided) at the top and/or footer

πŸ“˜ Content to Include:
The following content should be visually structured and formatted in clear, engaging blocks. We’ll provide this content in a PDF format

1. Header Title:
"VoltaKor 6 Week Autumn Forge Nutrition Blueprint"

2. Introduction (Small Block):
Short blurb about the challenge goals (lose body fat, gain energy, preserve lean muscle mass)

3. Elimination List (Foods to Avoid):
A visually separated section with a list of foods and drinks that should be eliminated or greatly reduced for fat loss

4. Smart Swaps Table:
A side-by-side "Craving vs Swap" table that shows easy alternatives to popular bad habits (e.g., soda β†’ sparkling water)

5. Build-Your-Own Meal Plan Sections:
Organize these into clear categories:

Proteins

Carbs

Fats

Veggies

Extras / Smart Swaps
Use icons, color codes, or visual grids to organize these food lists

6. Tips Section (Optional Bonuses):
Hydration goal

Suggested number of meals

Protein shake recommendation

Meal timing tip

10-min walk after dinner tip

πŸ“¦ Files Provided:

All written content in organized text format

βœ… Deliverables:
Final design in print-ready PDF

Editable source file (AI, PSD, or InDesign preferred)

πŸ™Œ Inspiration:
Design should feel in line with the type of professional print materials used by high-end fitness studios. Clean lines, engaging fonts, and premium layout. We're not looking for clipart or gimmicky stock photos β€” we want the design to reflect the premium, results-driven experience our gym provides.

```html
<!DOCTYPE html>
<html lang="en">
<head>
<meta charset="utf-8">
<title>VoltaKor 6 Week Autumn Forge Nutrition Blueprint</title>
<link href="https://fonts.googleapis.com/css2?family=Archivo+Black&family=Montserrat:ital,wght@0,400;0,500;0,700;0,800;1,400&display=swap" rel="stylesheet">
<style>
:root{
  --stage:#8c8c8c;
  --ink:#0c0c0c;
  --paper:#ffffff;
  --yellow:#f6d415;
  --red:#e02424;
  --orange:#f7931e;
  --blue:#3f51c4;
  --green:#5cb85c;
  --text:#e9e9e9;
}
*{box-sizing:border-box;margin:0;padding:0}
html,body{width:1200px;height:800px;overflow:hidden}
body{background:var(--stage);font-family:"Montserrat",sans-serif;color:var(--text);position:relative}
.side-label{position:absolute;top:24px;font-family:"Archivo Black",sans-serif;color:#fff;font-size:21px;letter-spacing:14px}
.page{position:absolute;background:var(--ink);overflow:hidden}
.page-front{left:48px;top:55px;width:537px;height:695px}
.page-back{left:619px;top:55px;width:540px;height:700px}
.photo-bg{position:absolute;inset:0;background:radial-gradient(ellipse at 55% 60%,#2a2a2a 0%,#141414 55%,#0a0a0a 100%)}
.abs{position:absolute}
.brand{font-family:"Archivo Black",sans-serif;color:#fff;line-height:1}
.brand-tag{font-family:"Montserrat",sans-serif;font-weight:700;color:var(--yellow);letter-spacing:2.4px;text-transform:uppercase;white-space:nowrap}
.badge{position:absolute;top:110px;height:37px;width:64px;display:flex;align-items:center;justify-content:center;text-align:center;font-family:"Archivo Black",sans-serif;font-size:6.5px;line-height:1.15;color:#fff;text-transform:uppercase}
.badge-orange{background:var(--orange)}
.badge-blue{background:var(--blue)}
.badge-green{background:var(--green)}
.tagline{left:47px;top:154px;font-size:7.5px;font-style:italic;color:#ddd}
.title-paper{left:243px;top:19px;width:300px;height:133px;background:var(--paper);clip-path:polygon(8% 4%,20% 0,45% 6%,70% 3%,100% 8%,100% 78%,80% 86%,55% 90%,30% 94%,3% 100%,0 55%,4% 25%)}
.title{left:324px;top:44px;font-family:"Archivo Black",sans-serif;line-height:1}
.title-weeks{font-size:40px;color:var(--blue);letter-spacing:-.5px}
.title-season{font-size:19.5px;color:var(--green);margin-top:2px}
.title-doc{font-size:14.5px;color:#111;margin-top:2px}
.band{position:absolute;background:var(--yellow);color:#111;font-family:"Archivo Black",sans-serif;display:flex;align-items:center;justify-content:center;text-align:center}
.band-eliminate{left:29px;top:181px;width:478px;height:31px;font-size:14px;white-space:nowrap;letter-spacing:-.3px}
.band-eliminate .soft{font-family:"Montserrat",sans-serif;font-weight:500;font-size:14.5px;margin-left:5px;letter-spacing:0}
.band-swaps{left:29px;top:416px;width:478px;height:31px;font-size:15.5px;white-space:nowrap}
.intro{left:36px;top:218px;width:464px;text-align:center;font-size:10.3px;line-height:1.3;color:#f2f2f2}
.ticks{list-style:none;position:absolute}
.ticks li{position:relative;padding-left:17px;font-size:9.3px;line-height:1.28;color:var(--text)}
.ticks li::before{content:"";position:absolute;left:0;top:1px;width:11px;height:11px;border-radius:50%;background:var(--red)}
.ticks li::after{content:"";position:absolute;left:3.6px;top:3.2px;width:3px;height:5px;border:solid #fff;border-width:0 1.6px 1.6px 0;transform:rotate(40deg)}
.front-list li{font-size:8.7px}
.avoid-left{left:38px;top:258px;width:235px}
.avoid-left li{margin-bottom:6.2px}
.avoid-right{left:281px;top:258px;width:245px}
.avoid-right li{margin-bottom:12.6px}
.vertical{position:absolute;font-family:"Archivo Black",sans-serif;color:#fff;writing-mode:vertical-rl;transform:rotate(180deg);letter-spacing:1.5px}
.craving-label{left:32px;top:462px;font-size:14px}
.instead-label{left:161px;top:462px;font-size:14px}
.rule{position:absolute;width:1px;background:#cfcfcf}
.craving-list{left:59px;top:463px;width:100px}
.craving-list li{font-weight:700;font-size:9.3px;margin-bottom:5.4px;color:#fff}
.instead-list{left:189px;top:463px;width:345px}
.instead-list li{margin-bottom:5.4px;white-space:nowrap;font-size:8.6px;line-height:1.39}
.footer-paper{left:0;top:657px;width:537px;height:38px;background:var(--paper);clip-path:polygon(0 18%,6% 8%,14% 16%,24% 5%,36% 14%,48% 6%,60% 15%,72% 4%,84% 13%,94% 6%,100% 12%,100% 100%,0 100%)}
.site{left:0;top:673px;width:537px;text-align:center;font-size:11px;font-weight:800;letter-spacing:1.2px;color:#111}
.band-plan{left:19px;top:19px;width:503px;height:85px;flex-direction:column;clip-path:polygon(0 6%,10% 2%,25% 5%,45% 0,65% 4%,85% 1%,100% 5%,100% 95%,80% 99%,55% 96%,30% 100%,10% 96%,0 99%)}
.band-plan h2{font-size:15.5px;letter-spacing:-.2px}
.band-plan p{font-family:"Montserrat",sans-serif;font-size:10px;line-height:1.35;margin-top:5px;padding:0 24px;color:#222}
.icon-art{position:absolute;border-radius:50%}
.group-head{position:absolute;line-height:1}
.group-head h3{font-family:"Archivo Black",sans-serif;font-size:15px;color:#fff}
.group-head p{font-size:12.5px;line-height:1.15;color:#fff;margin-top:2px}
.food li{font-size:9.4px;margin-bottom:2.6px;line-height:1.15}
.box-frame{position:absolute;border:1px solid var(--yellow)}
.box-head{font-size:12px;line-height:1.3}
.tip{position:absolute;display:flex;gap:6px;width:140px}
.tip .dot{flex:none;width:19px;height:19px;border-radius:50%}
.tip p{font-size:7px;line-height:1.3;color:#ddd}
.tip b{color:#fff;font-weight:700}
.habit{position:absolute;left:328px;display:flex;gap:10px;align-items:flex-start;width:185px}
.habit svg{flex:none}
.habit p{font-size:7.6px;line-height:1.35;color:#ddd}
</style>
</head>
<body>
  <div class="side-label" style="left:253px">FRONT</div>
  <div class="side-label" style="left:842px">BACK</div>

  <section class="page page-front">
    <div class="photo-bg" role="img" aria-label="Dark background photo of athletes training in a gym"></div>

    <div class="abs" style="left:36px;top:26px">
      <div class="brand" style="font-size:42px">VoltaKor</div>
      <div class="brand-tag" style="font-size:6.5px;margin-top:7px;margin-left:20px">Personal Group Training</div>
    </div>

    <div class="badge badge-orange" style="left:28px">Lose<br>Body Fat</div>
    <div class="badge badge-blue" style="left:97px">Gain<br>Energy</div>
    <div class="badge badge-green" style="left:165px">Preserve<br>Lean Muscle<br>Mass</div>
    <p class="abs tagline">without giving up real food or living in the kitchen.</p>

    <div class="abs title-paper" role="img" aria-label="Torn white paper panel"></div>
    <h1 class="abs title">
      <div class="title-weeks">6 WEEK</div>
      <div class="title-season">AUTUMN FORGE</div>
      <div class="title-doc">NUTRITION BLUEPRINT</div>
    </h1>

    <h2 class="band band-eliminate">FOODS &amp; DRINKS TO ELIMINATE<span class="soft">(OR GREATLY REDUCE)</span></h2>
    <p class="abs intro">These are the biggest culprits sabotaging fat loss — highly palatable, calorie-dense, and metabolically disruptive:</p>

    <ul class="ticks front-list avoid-left">
      <li>Sugary drinks (sodas, energy drinks, sweet teas, juice blends)</li>
      <li>Fancy coffee drinks (Frostaccinos, sugary creamers, flavor pumps)</li>
      <li>Fast food and fried foods (even “grilled” items often packed with oils)</li>
      <li>Packaged snacks (chips, cookies, granola bars, trail mix with candy)</li>
      <li>Baked goods (donuts, muffins, pastries, bagels with cream cheese)</li>
    </ul>
    <ul class="ticks front-list avoid-right">
      <li>Alcohol (especially beer and sugary mixers)</li>
      <li>Processed carbs (white breads, crackers, pasta)</li>
      <li>Cheese-heavy meals (pizza, nachos, quesadillas)</li>
      <li>High-fat deli meats (salami, pepperoni, sausage)</li>
      <li>Sauces and condiments loaded with sugar (ketchup, BBQ sauce, honey mustard)</li>
    </ul>

    <h2 class="band band-swaps">SMART SWAPS FOR FAT LOSS</h2>

    <div class="vertical craving-label">CRAVING</div>
    <div class="rule" style="left:39px;top:546px;height:110px"></div>
    <div class="vertical instead-label">TRY THIS INSTEAD</div>
    <div class="rule" style="left:169px;top:636px;height:20px"></div>

    <ul class="ticks craving-list">
      <li>Soda</li><li>Fancy Coffee</li><li>Chips</li><li>Ice Cream</li><li>Candy</li>
      <li>Pasta</li><li>Pizza</li><li>Alcohol</li><li>Sandwich Bread</li><li>Heavy Sauces</li>
    </ul>
    <ul class="ticks instead-list">
      <li>Sparkling water with lime, Fizzora, or plain water with fruit infusions</li>
      <li>Coffee with unsweetened almond milk + stevia drops or cinnamon</li>
      <li>Rice cakes, roasted chickpeas, or crunchy cucumber with Tavío</li>
      <li>Frozen banana blended with protein powder (DIY "nice cream")</li>
      <li>Berries, apples or dark chocolate squares (85%+)</li>
      <li>Zucchini noodles, chickpea pasta, or cauliflower rice</li>
      <li>Egg white wraps or low-carb tortillas with turkey pepperoni and light cheese</li>
      <li>Limit to 1x/week if needed</li>
      <li>Ezrin bread, low-carb wraps, or lettuce wraps</li>
      <li>Mustard, salsa, hot sauce, coconut aminos, Greek yogurt-based dips</li>
    </ul>

    <div class="abs footer-paper"></div>
    <div class="abs site">www.voltakor.com</div>
  </section>

  <section class="page page-back">
    <div class="photo-bg" role="img" aria-label="Dark background photo of a gym with weight plates"></div>

    <div class="band band-plan">
      <h2>BUILD-YOUR-OWN MEAL PLAN GUIDE</h2>
      <p>Use these fit-friendly food lists to mix &amp; match meals. Your job: choose 1 protein, 1 carb (if desired), and 1 fat or veggie at each meal. Keep it simple, keep it consistent.</p>
    </div>

    <div class="icon-art" style="left:40px;top:127px;width:40px;height:40px;background:linear-gradient(135deg,#fff 40%,#f59a1b 41%)" role="img" aria-label="Illustration of halved boiled eggs"></div>
    <div class="group-head" style="left:91px;top:126px">
      <h3>PROTEINS</h3>
      <p>(choose 1 per meal<br>/snack)</p>
    </div>
    <ul class="ticks food" style="left:41px;top:180px;width:240px">
      <li>Chicken breast or thighs (air fried or grilled)</li>
      <li>Lean ground beef (90/10 or better)</li>
      <li>Ground turkey or turkey breast</li>
      <li>Center-cut pork chops</li>
      <li>Eggs / Egg whites</li>
      <li>Tuna (canned in water)</li>
      <li>Salmon or white fish</li>
      <li>Shrimp</li>
      <li>Greek yogurt (plain, low sugar)</li>
      <li>Cottage cheese (low-fat)</li>
      <li>Protein powder (whey or plant-based)</li>
      <li>Deli turkey (low-sodium)</li>
    </ul>

    <div class="icon-art" style="left:281px;top:128px;width:42px;height:40px;border-radius:8px;background:linear-gradient(90deg,#c8782e,#f0e6d6 60%,#a85a2a)" role="img" aria-label="Illustration of a rice bowl and bread loaf"></div>
    <div class="group-head" style="left:333px;top:126px">
      <h3>CARBS</h3>
      <p>(choose 1–2 servings per day,<br>timed post-workout or morning)</p>
    </div>
    <ul class="ticks food" style="left:282px;top:180px;width:240px">
      <li>Jasmine or basmati rice (white or brown)</li>
      <li>Sweet potatoes or yams</li>
      <li>Rolled oats or steel cut oats</li>
      <li>Quinoa</li>
      <li>Ezrin bread</li>
      <li>Rice cakes</li>
      <li>Berries (blueberries, raspberries, strawberries)</li>
      <li>Apples / Bananas</li>
      <li>Chickpeas or black beans (in moderation)</li>
    </ul>

    <div class="icon-art" style="left:37px;top:346px;width:44px;height:46px;border-radius:40%;background:linear-gradient(135deg,#8bc34a,#4e8a2a)" role="img" aria-label="Illustration of a halved avocado"></div>
    <div class="group-head" style="left:91px;top:348px">
      <h3>FATS</h3>
      <p>&nbsp;(add small amounts to<br>meals, 2–4 servings/day)</p>
    </div>
    <ul class="ticks food" style="left:41px;top:402px;width:240px">
      <li>Avocado or guacamole</li>
      <li>Olive oil or avocado oil (cooking or drizzle)</li>
      <li>Nut butters (almond, peanut – natural only)</li>
      <li>Whole eggs</li>
      <li>Nuts (almonds, walnuts – portion controlled)</li>
      <li>Chia seeds or flax seeds</li>
    </ul>

    <div class="icon-art" style="left:280px;top:317px;width:46px;height:44px;border-radius:40%;background:linear-gradient(135deg,#f28a2e,#ef3e5b)" role="img" aria-label="Illustration of a carrot and tomato"></div>
    <div class="group-head" style="left:335px;top:318px">
      <h3>VEGGIES</h3>
      <p>(unlimited – fill your<br>plate!)</p>
    </div>
    <ul class="ticks food" style="left:282px;top:370px;width:245px">
      <li>Spinach, kale, arugula</li>
      <li>Zucchini, asparagus, bell peppers</li>
      <li>Broccoli, cauliflower, green beans</li>
      <li>Cucumber, tomatoes, shredded carrots</li>
      <li>Mixed greens or salad kits (watch the dressing)</li>
    </ul>

    <div class="abs" style="left:284px;top:447px">
      <div class="brand" style="font-size:27px">VoltaKor</div>
      <div class="brand-tag" style="font-size:5px;margin-top:5px;margin-left:12px;letter-spacing:1.5px">Personal Group Training</div>
    </div>

    <div class="box-frame" style="left:20px;top:521px;width:278px;height:164px"></div>
    <h3 class="band box-head" style="left:32px;top:497px;width:255px;height:45px">BONUS TIPS FOR MAXIMUM<br>RESULTS</h3>

    <div class="tip" style="left:33px;top:555px"><span class="dot" style="background:#d9dde8" role="img" aria-label="Water drinking icon"></span><p><b>Drink 80–120 oz. water daily</b> hydration is key for fat loss and muscle performance</p></div>
    <div class="tip" style="left:177px;top:555px;width:118px"><span class="dot" style="background:#e8c07a" role="img" aria-label="Meal plate icon"></span><p><b>Eat 3–4 meals per day</b> spaced every 3–4 hours</p></div>
    <div class="tip" style="left:33px;top:594px"><span class="dot" style="background:#cfd6f0" role="img" aria-label="Protein plate icon"></span><p><b>Include protein in every meal</b> to stabilize blood sugar and support muscle</p></div>
    <div class="tip" style="left:177px;top:594px;width:118px"><span class="dot" style="background:#e9a07c" role="img" aria-label="Post-workout meal icon"></span><p><b>Post-workout meal = protein + carb</b> no added fats</p></div>
    <div class="tip" style="left:33px;top:634px"><span class="dot" style="background:#6fbf8a" role="img" aria-label="Protein shaker icon"></span><p><b>Up to, two protein shakes per day is allowed</b> especially post-workout or on busy days</p></div>
    <div class="tip" style="left:177px;top:634px;width:118px"><span class="dot" style="background:#ef6fa0" role="img" aria-label="Donut icon"></span><p><b>Limit “treat” meals to 1 per week</b> (keep it controlled)</p></div>

    <div class="box-frame" style="left:304px;top:521px;width:222px;height:164px"></div>
    <h3 class="band box-head" style="left:308px;top:497px;width:211px;height:45px">OPTIONAL HABITS<br>TO STACK</h3>

    <div class="habit" style="top:560px"><svg width="19" height="19" viewBox="0 0 20 20"><circle cx="10" cy="10" r="9.5" fill="#f6d415"/><path d="M5.5 10.3l3 3 6-6.3" fill="none" stroke="#111" stroke-width="2"/></svg><p>Weigh in once per week<br>(same day/time)</p></div>
    <div class="habit" style="top:590px"><svg width="19" height="19" viewBox="0 0 20 20"><circle cx="10" cy="10" r="9.5" fill="#f6d415"/><path d="M5.5 10.3l3 3 6-6.3" fill="none" stroke="#111" stroke-width="2"/></svg><p>Prep 2–3 proteins and veggies<br>on Sunday</p></div>
    <div class="habit" style="top:620px"><svg width="19" height="19" viewBox="0 0 20 20"><circle cx="10" cy="10" r="9.5" fill="#f6d415"/><path d="M5.5 10.3l3 3 6-6.3" fill="none" stroke="#111" stroke-width="2"/></svg><p>Keep a visible “YES/NO” food list on<br>the fridge</p></div>
    <div class="habit" style="top:651px"><svg width="19" height="19" viewBox="0 0 20 20"><circle cx="10" cy="10" r="9.5" fill="#f6d415"/><path d="M5.5 10.3l3 3 6-6.3" fill="none" stroke="#111" stroke-width="2"/></svg><p>Add a short 10-min walk after dinner to<br>boost digestion</p></div>
  </section>
</body>
</html>
```